Brisk Ledger Hub's Facebook Cover Design

I am in need of a social media cover for my company's Facebook account. Please leverage the green logos and color palette attached.

Brisk Ledger Hub offers 2 primary services:
1.) Business Automation Services
2.) AI (artificial intelligence integrations)

While a lot of what we do is highly technical, what we deliver is not. In a nutshell, we help our clients to connect their data regardless of what application that data is sitting in. Because we can connect that data, often times we can:

A.) offer more intelligent marketing and help our client increase their revenue.
B.) automate highly repetitive tasks using technology and drive down their costs thus saving them money
C.) help our clients use AI to better serve their customers

You can read a little bit about our company here: https://www.briskledgerhub.example

Our tagline is: "Connect data to increase the flow of profitability."

Visually, we'd like your help to illustrate the "connecting" of these applications. Please let me know if you have any questions.

Target Market(s)

Business Owners or Marketing Managers

Industry/Entity Type

Marketing technologies.

Font styles to use
Sans Serif

Requirements
Must have
• Please make every effort to have the cover compatible with the color palette of the attached images.
Should not have
• Please do not use the standard clipart or stock libraries of AI = robot. If you do, please make them small. We help business glue their data from different sources to solve real work problems. Little robots are overused.

```html
<!DOCTYPE html>
<html lang="en">
<head>
<meta charset="utf-8">
<title>Brisk Ledger Hub – Cover</title>
<link rel="stylesheet" href="https://fonts.googleapis.com/css2?family=Poppins:wght@700&display=swap">
<style>
  :root {
    --leaf-green: #8cc65a;
    --paper-white: #ffffff;
    --ink-grey: #58595b;
    --globe-blue: #5aa9e6;
    --globe-ring: #4cb050;
    --cloud-grey: #e6e8ec;
    --node-red: #d9453a;
    --node-yellow: #e9b21c;
    --node-blue: #3f9fe0;
    --rocket-white: #f1f3f6;
    --rocket-blue: #4b9be0;
  }
  * { margin: 0; padding: 0; box-sizing: border-box; }
  html, body { width: 1200px; height: 457px; overflow: hidden; background: var(--paper-white); }
  .cover {
    position: relative;
    width: 1200px;
    height: 457px;
    overflow: hidden;
    background: var(--leaf-green);
    font-family: "Poppins", sans-serif;
  }
  .cover__shapes { position: absolute; inset: 0; }
  .cover__shapes path { fill: var(--paper-white); }
  .brand-name {
    position: absolute;
    top: 44px;
    left: 0;
    width: 1200px;
    text-align: center;
    color: var(--paper-white);
    font-weight: 700;
    font-size: 33px;
    letter-spacing: -0.5px;
  }
  .tagline {
    position: absolute;
    top: 190px;
    left: 250px;
    width: 500px;
    text-align: center;
    color: var(--ink-grey);
    font-weight: 700;
    font-size: 41px;
    line-height: 55px;
  }
  .art { position: absolute; }
  .art--globe {
    left: 100px; top: 48px; width: 170px; height: 122px;
    border-radius: 50%;
    background: radial-gradient(circle at 45% 40%, var(--paper-white) 0 25%, var(--globe-blue) 55%, var(--globe-ring) 100%);
  }
  .art--cloud {
    left: 915px; top: 40px; width: 180px; height: 185px;
    border-radius: 45% 45% 30% 30%;
    background: radial-gradient(ellipse at 50% 30%, var(--cloud-grey) 0 50%, var(--node-blue) 75%, var(--node-red) 88%, var(--node-yellow) 100%);
  }
  .art--rocket {
    left: 815px; top: 330px; width: 150px; height: 88px;
    border-radius: 50% 40% 40% 50%;
    background: linear-gradient(135deg, var(--rocket-white) 0 55%, var(--rocket-blue) 100%);
  }
</style>
</head>
<body>
  <main class="cover">
    <svg class="cover__shapes" width="1200" height="457" viewBox="0 0 1200 457" aria-hidden="true">
      <path class="shape shape--corner" d="M0,0 H330 C250,20 150,40 90,80 C50,105 20,110 0,110 Z"/>
      <path class="shape shape--centre" d="M120,457 C150,350 170,250 260,200 C340,160 380,120 470,110 C560,100 640,105 720,120 C820,140 860,200 840,290 C820,370 780,420 790,457 Z"/>
      <path class="shape shape--cloud-bed" d="M870,0 H1200 V190 C1140,210 1110,260 1080,310 C1040,370 960,360 920,300 C880,240 880,160 900,100 C910,60 880,20 870,0 Z"/>
      <path class="shape shape--foot" d="M1010,457 C1040,400 1090,330 1150,310 C1180,300 1200,305 1200,305 V457 Z"/>
    </svg>

    <div class="brand-name">Brisk Ledger Hub</div>

    <h1 class="tagline">Connect data to increase the flow of profitability.</h1>

    <div class="art art--globe" role="img" aria-label="3D globe with a green orbit arrow and red location pins"></div>
    <div class="art art--cloud" role="img" aria-label="3D cloud connected by lines to red, yellow and blue nodes"></div>
    <div class="art art--rocket" role="img" aria-label="3D white and blue rocket with a puff of smoke"></div>
  </main>
</body>
</html>
```